依頼概要
・株式会社森岡ホールディングスの社員募集のポスター作成して頂きたいです。

・詳細 黒を基調としたシンプルな感じなのですが、目にとまるインパクトさも必要。
『社員募集』は英語表記で『資格保有者優遇』(日本語OK)のワードは入れてほしい    です。
添付データの右上の会社ロゴの『MOKA』を背景に透かして入れてほしいです。

・ 重視する点 過去・現在までにデザインの経験のある方を希望致します。

・その他何かご不明な点がございましたら、お気軽にご質問下さい。
よろしくお願いいたします。
■ 選んだ理由

黒を基調のシンプルさの中にインパクトのあるデザインで気に入りました。

■ 提案者全員のお礼・コメント

この度は沢山の提案をして頂きありがとうございます。
また、機会があれば宜しくお願い致します。

```html
<!DOCTYPE html>
<html lang="ja">
<head>
<meta charset="utf-8">
<title>社員募集ポスター｜株式会社森岡ホールディングス</title>
<link href="https://fonts.googleapis.com/css2?family=Shippori+Mincho:wght@500;700;800&family=Playfair+Display:ital,wght@1,500&family=Noto+Sans+JP:wght@500&display=swap" rel="stylesheet">
<style>
  :root{
    --page:#eeeeec;
    --paper:#ffffff;
    --ink:#141414;
    --sky-top:#3f7fc6;
    --sky-mid:#8fb9e3;
    --sky-pale:#dfeaf5;
    --accent:#2f6fb6;
    --badge:#1f3f73;
    --city:#7d9cc0;
  }
  *{margin:0;padding:0;box-sizing:border-box}
  html,body{width:849px;height:1200px;overflow:hidden;background:var(--page)}
  .poster{
    position:absolute;left:75px;top:105px;width:700px;height:990px;
    background:var(--paper);overflow:hidden;
    box-shadow:0 2px 10px rgba(0,0,0,.12);
  }
  .poster-art{position:absolute;inset:0;width:700px;height:990px}
  .headline{
    position:absolute;right:46px;top:150px;
    writing-mode:vertical-rl;
    font-family:"Shippori Mincho",serif;font-weight:800;
    font-size:118px;line-height:1;letter-spacing:.02em;color:var(--ink);
  }
  .company{
    position:absolute;left:454px;top:430px;
    writing-mode:vertical-rl;
    font-family:"Shippori Mincho",serif;font-weight:700;
    font-size:24px;line-height:1;color:var(--ink);white-space:nowrap;
    display:flex;align-items:center;gap:8px;
  }
  .company-mark{width:16px;height:16px;background:var(--ink)}
  .details{
    position:absolute;left:398px;top:458px;
    writing-mode:vertical-rl;
    font-family:"Noto Sans JP",sans-serif;font-weight:500;
    font-size:12px;line-height:18px;color:var(--ink);
  }
  .english-title{
    position:absolute;left:-128px;top:560px;width:420px;
    transform:rotate(-90deg);transform-origin:center;
    font-family:"Playfair Display",serif;font-style:italic;font-weight:500;
    font-size:46px;line-height:1;color:var(--accent);white-space:nowrap;
  }
  .badge{
    position:absolute;left:427px;top:835px;width:78px;height:78px;border-radius:50%;
    background:var(--badge);color:#fff;
    display:flex;flex-direction:column;align-items:center;justify-content:center;
    font-family:"Shippori Mincho",serif;font-weight:700;
  }
  .badge-sub{font-size:9px;line-height:1.2}
  .badge-main{font-size:20px;line-height:1.1}
</style>
</head>
<body>
<main class="poster">
  <svg class="poster-art" viewBox="0 0 700 990">
    <defs>
      <linearGradient id="sky" x1="0" y1="0" x2="0" y2="1">
        <stop offset="0" stop-color="#3f7fc6"/>
        <stop offset=".55" stop-color="#8fb9e3"/>
        <stop offset="1" stop-color="#dfeaf5"/>
      </linearGradient>
      <linearGradient id="person" x1="0" y1="0" x2="1" y2="1">
        <stop offset="0" stop-color="#c9d8e8"/>
        <stop offset="1" stop-color="#eef2f6"/>
      </linearGradient>
      <linearGradient id="city" x1="0" y1="0" x2="0" y2="1">
        <stop offset="0" stop-color="#7d9cc0"/>
        <stop offset="1" stop-color="#c7d6e7"/>
      </linearGradient>
    </defs>
    <rect class="sky-photo" x="20" y="20" width="660" height="860" fill="url(#sky)" role="img" aria-label="青空と雲の写真"/>
    <polygon class="divider" points="150,20 215,20 90,880 25,880" fill="#ffffff" opacity=".85"/>
    <polygon class="photo-worker" points="40,160 205,160 150,560 40,560" fill="url(#person)" role="img" aria-label="ヘルメットをかぶった若い男性作業員の写真"/>
    <polygon class="photo-office" points="250,20 470,20 440,360 220,360" fill="url(#person)" role="img" aria-label="空を見上げる若い女性社員の写真"/>
    <rect class="photo-city" x="20" y="760" width="660" height="130" fill="url(#city)" role="img" aria-label="高層ビルが並ぶ都市の写真"/>
  </svg>

  <h1 class="headline">集え若者。</h1>
  <p class="company"><span class="company-mark"></span>株式会社森岡ホールディングス</p>
  <p class="details">営業職・施工管理・設計<br>勤務地 本社・各支店<br>正社員 経験者歓迎</p>
  <p class="english-title">Recruitment of employees</p>
  <div class="badge"><span class="badge-sub">資格保有者</span><span class="badge-main">優遇</span></div>
</main>
</body>
</html>
```